BRL business card

For a business card with our logo

Contact Information for Business Card

Mathéo VRANEL
Founder & CEO
email : ceo@brightlanterncollective.com / www.brightlanterncollective.com /
instagram / facebook / WhatsApp
N°: +590 690 482 517

Colors

Designer to choose colors to be used in the design.

```html
<!DOCTYPE html>
<html lang="en">
<head>
<meta charset="utf-8">
<title>BRL Business Card</title>
<link rel="stylesheet" href="https://fonts.googleapis.com/css2?family=Cinzel:wght@600&family=Montserrat:wght@600;700&family=Questrial&display=swap">
<style>
  :root {
    --brand-orange: #f37327;
    --brand-orange-soft: #f4a478;
    --brand-blue: #0c58a6;
    --ink: #111111;
    --paper: #ffffff;
    --backdrop: #e6ddd4;
  }
  html, body {
    margin: 0;
    padding: 0;
    width: 1200px;
    height: 1200px;
    overflow: hidden;
    background: var(--backdrop);
  }
  .canvas {
    position: relative;
    width: 1200px;
    height: 1200px;
  }
  .card {
    position: absolute;
    left: 196px;
    width: 786px;
    height: 449px;
    background: var(--paper);
    box-shadow: 0 18px 30px rgba(0,0,0,0.18);
  }
  .card--front { top: 76px; }
  .card--back { top: 568px; }
  .card svg { display: block; width: 100%; height: 100%; }
  .wordmark { font-family: "Cinzel", serif; font-weight: 600; fill: var(--brand-blue); }
  .social-label { font-family: "Questrial", sans-serif; fill: var(--paper); }
  .person-first { font-family: "Questrial", sans-serif; fill: var(--ink); }
  .person-last { font-family: "Montserrat", sans-serif; font-weight: 700; fill: var(--ink); }
  .person-role { font-family: "Questrial", sans-serif; fill: var(--brand-orange-soft); }
  .contact-line { font-family: "Montserrat", sans-serif; font-weight: 600; fill: var(--ink); }
  .contact-accent { fill: var(--brand-orange); font-weight: 600; }
</style>
</head>
<body>
<main class="canvas">

  <section class="card card--front" aria-label="Card front">
    <svg viewBox="0 0 1267 724" xmlns="http://www.w3.org/2000/svg">
      <circle class="brand-dot" cx="628" cy="250" r="100" fill="var(--brand-orange)"/>
      <text class="wordmark" x="628" y="428" text-anchor="middle" font-size="60">BRIGHT LANTERN</text>
      <text class="wordmark" x="628" y="470" text-anchor="middle" font-size="34" letter-spacing="18">COLLECTIVE</text>

      <path class="wave-orange" fill="var(--brand-orange)"
        d="M0,461 C180,458 300,500 420,540 C620,620 900,640 1267,518 V724 H0 Z"/>
      <path class="wave-blue" fill="var(--brand-blue)"
        d="M380,522 C600,600 900,630 1267,437 V500 C950,640 650,630 380,522 Z"/>

      <text class="social-label" x="68" y="583" font-size="23">Join us on social media!</text>
      <g class="social-links" fill="none" stroke="var(--paper)" stroke-width="3">
        <circle cx="101" cy="633" r="30" role="img" aria-label="Social profile link one"/>
        <circle cx="192" cy="633" r="30" role="img" aria-label="Social profile link two"/>
        <circle cx="283" cy="633" r="30" role="img" aria-label="Messaging contact link"/>
      </g>
    </svg>
  </section>

  <section class="card card--back" aria-label="Card back">
    <svg viewBox="0 0 1267 724" xmlns="http://www.w3.org/2000/svg">
      <path class="wave-orange" fill="var(--brand-orange)"
        d="M0,0 H1035 C900,40 700,55 560,52 C300,50 120,110 0,205 Z"/>
      <path class="wave-blue" fill="var(--brand-blue)"
        d="M310,724 C500,660 700,650 900,645 C1100,640 1200,580 1267,535 V724 Z"/>

      <circle class="brand-dot" cx="243" cy="362" r="62" fill="var(--brand-orange)"/>
      <text class="wordmark" x="243" y="470" text-anchor="middle" font-size="40">BRL</text>

      <text x="463" y="197" font-size="68"><tspan class="person-first">Mathéo </tspan><tspan class="person-last">VRANEL</tspan></text>
      <text class="person-role" x="728" y="245" text-anchor="middle" font-size="40">Founder &amp; CEO</text>

      <g class="contact-icons">
        <circle cx="509" cy="329" r="33" fill="var(--brand-blue)"/>
        <rect x="498" y="310" width="22" height="36" rx="3" fill="none" stroke="var(--paper)" stroke-width="3"/>
        <circle cx="509" cy="340" r="2.5" fill="var(--paper)"/>

        <circle cx="509" cy="416" r="33" fill="var(--brand-blue)"/>
        <rect x="492" y="404" width="34" height="24" rx="2" fill="none" stroke="var(--paper)" stroke-width="3"/>
        <path d="M492,406 L509,419 L526,406" fill="none" stroke="var(--paper)" stroke-width="3"/>

        <circle cx="509" cy="502" r="33" fill="var(--brand-blue)"/>
        <g fill="none" stroke="var(--paper)" stroke-width="2.5">
          <circle cx="509" cy="502" r="18"/>
          <ellipse cx="509" cy="502" rx="8" ry="18"/>
          <line x1="491" y1="502" x2="527" y2="502"/>
          <line x1="494" y1="493" x2="524" y2="493"/>
          <line x1="494" y1="511" x2="524" y2="511"/>
        </g>
      </g>

      <text class="contact-line" x="560" y="340" font-size="33">+590 690 482 517</text>
      <text class="contact-line" x="562" y="417" font-size="31">ceo@<tspan class="contact-accent">brightlanterncollective</tspan>.com</text>
      <text class="contact-line" x="562" y="512" font-size="31">www.<tspan class="contact-accent">brightlanterncollective</tspan>.com</text>
    </svg>
  </section>

</main>
</body>
</html>
```